Business card/ stationary design for a pressure washing company
Commercial and Residential
Business card/ stationary design for a pressure washing company - Cleaning
Creative Brief
Simple
Marcus Delgado
N/A
Brookrinse@mailbox-demo.com
www.brookrinse-demo.com
Open to the idea of single or double sided business cards
brookrinse brookrinse
I have gone through the submissions that I have received so far and indicated a couple from each designer that I like. If you could please take that and apply it into a full stationary demo as well as a vehicle magnet, I would love to see how the design ideas transfer into the various applications. Thanks, Marcus
Also, a vehicle magnet would be very useful. Thanks!

```html
<!DOCTYPE html>
<html lang="en">
<head>
<meta charset="utf-8">
<title>Brookrinse Business Card</title>
<link href="https://fonts.googleapis.com/css2?family=Open+Sans:wght@400;600;800&display=swap" rel="stylesheet">
<style>
  :root {
    --backdrop: #3a3a3c;
    --card: #ffffff;
    --brand-blue: #1f3fae;
    --bright-blue: #2f7de1;
    --navy: #14256e;
    --ink: #3b3b3b;
    --muted: #6b6b6b;
  }
  * { margin: 0; padding: 0; box-sizing: border-box; }
  html, body { width: 1200px; height: 902px; overflow: hidden; }
  body {
    background: var(--backdrop);
    font-family: "Open Sans", Arial, sans-serif;
    position: relative;
  }
  .card {
    position: absolute;
    left: 250px;
    width: 700px;
    height: 400px;
    background: var(--card);
    border-radius: 14px;
    overflow: hidden;
    box-shadow: 0 10px 30px rgba(0,0,0,.35);
  }
  .card-back { top: 40px; }
  .card-front { top: 462px; }

  .brand {
    display: flex;
    align-items: center;
    gap: 14px;
    color: var(--brand-blue);
    font-weight: 800;
    letter-spacing: 1px;
  }
  .brand-dot {
    border-radius: 50%;
    background: var(--bright-blue);
    flex: none;
  }
  .card-back .brand {
    position: absolute;
    left: 150px;
    top: 130px;
    font-size: 58px;
  }
  .card-back .brand-dot { width: 40px; height: 40px; }
  .website {
    position: absolute;
    left: 210px;
    top: 240px;
    font-size: 20px;
    color: var(--muted);
    letter-spacing: .5px;
  }

  .card-front .brand {
    position: absolute;
    left: 44px;
    top: 54px;
    font-size: 42px;
  }
  .card-front .brand-dot { width: 30px; height: 30px; }
  .holder {
    position: absolute;
    right: 54px;
    top: 52px;
    text-align: left;
    width: 230px;
  }
  .holder-name {
    font-size: 24px;
    font-weight: 600;
    color: var(--brand-blue);
  }
  .holder-role {
    font-size: 15px;
    color: var(--muted);
    margin-top: 2px;
  }
  .contacts {
    position: absolute;
    right: 38px;
    top: 222px;
    list-style: none;
    text-align: right;
    font-size: 17px;
    color: var(--ink);
    line-height: 27px;
  }
  .contacts li { display: flex; justify-content: flex-end; align-items: center; gap: 8px; }
  .contacts svg { width: 14px; height: 14px; fill: var(--brand-blue); }
  .contacts .email { margin-top: 12px; font-size: 15px; }
  .swoosh { position: absolute; left: 0; bottom: 0; width: 700px; height: 400px; }
</style>
</head>
<body>
  <section class="card card-back">
    <div class="brand"><span class="brand-dot"></span>BROOKRINSE</div>
    <p class="website">www.brookrinse-demo.com</p>
  </section>

  <section class="card card-front">
    <svg class="swoosh" viewBox="0 0 700 400" aria-hidden="true">
      <path d="M0 262 C160 250 300 290 420 340 C470 362 520 384 560 400 L0 400 Z" fill="var(--bright-blue)"/>
      <path d="M0 282 C170 272 310 312 420 358 C450 372 480 388 500 400 L0 400 Z" fill="#ffffff"/>
      <path d="M0 298 C180 290 320 330 420 374 C440 383 455 392 470 400 L0 400 Z" fill="var(--brand-blue)"/>
      <path d="M0 340 C150 334 260 360 330 400 L0 400 Z" fill="var(--navy)"/>
    </svg>
    <div class="brand"><span class="brand-dot"></span>BROOKRINSE</div>
    <div class="holder">
      <p class="holder-name">Marcus Delgado</p>
      <p class="holder-role">Managing Director</p>
    </div>
    <ul class="contacts">
      <li>123 456 7890
        <svg viewBox="0 0 24 24"><path d="M6.6 10.8a15 15 0 0 0 6.6 6.6l2.2-2.2a1 1 0 0 1 1-.25 11.4 11.4 0 0 0 3.6.57 1 1 0 0 1 1 1V20a1 1 0 0 1-1 1A17 17 0 0 1 3 4a1 1 0 0 1 1-1h3.5a1 1 0 0 1 1 1c0 1.25.2 2.45.57 3.57a1 1 0 0 1-.25 1z"/></svg>
      </li>
      <li>123 456 7890
        <svg viewBox="0 0 24 24"><path d="M6 3h12v5H6zM4 9h16a2 2 0 0 1 2 2v6h-4v4H6v-4H2v-6a2 2 0 0 1 2-2zm4 7v3h8v-3z"/></svg>
      </li>
      <li class="email">Brookrinse@mailbox-demo.com
        <svg viewBox="0 0 24 24"><path d="M2 5h20v14H2zm2 2v.5l8 5 8-5V7z"/></svg>
      </li>
    </ul>
  </section>
</body>
</html>
```